CV design and layout with option for text and contact details has be sleek

I have logo just need this to look good on a CV

Target Market(s)

Directors , Production , TV, Film

Industry/Entity Type

tv film cinema advertising

Colors
0054AA
0677BA
7BADD7
CADEEF
E8F1F8

Requirements
Must have
• my logo and contact information
Should not have
• any other images or logos except mine

```html
<!DOCTYPE html>
<html lang="en">
<head>
<meta charset="utf-8">
<title>Daniel Reeve – Cinematographer CV</title>
<link rel="stylesheet" href="https://fonts.googleapis.com/css2?family=Montserrat:wght@400;500;600;700&display=swap">
<style>
  :root {
    --backdrop: #dedbdc;
    --paper: #ffffff;
    --panel: #cdeefb;
    --ink: #111111;
    --rule: #bfe4f5;
  }
  * { margin: 0; padding: 0; box-sizing: border-box; }
  html, body { width: 1000px; height: 1200px; overflow: hidden; }
  body { background: var(--backdrop); font-family: "Montserrat", sans-serif; color: var(--ink); }
  .page { position: absolute; left: 115px; top: 56px; width: 770px; height: 1088px; background: var(--paper); }
  .side-panel { position: absolute; left: 0; top: 249px; width: 250px; height: 839px; background: var(--panel); }
  .header-divider { position: absolute; left: 249px; top: 0; width: 1px; height: 249px; background: var(--rule); }

  .brand { position: absolute; left: 0; top: 108px; width: 250px; text-align: center; white-space: nowrap; }
  .brand-name { display: block; font-size: 17px; font-weight: 400; letter-spacing: 0.3px; line-height: 22px; }
  .brand-role { display: block; font-size: 10px; font-weight: 400; letter-spacing: 0.6px; line-height: 13px; }

  .contact { position: absolute; left: 279px; top: 67px; font-size: 10.5px; font-weight: 500; }
  .contact-row { display: flex; height: 25px; }
  .contact-label { width: 107px; }

  .band { position: absolute; left: 250px; width: 520px; height: 20px; background: var(--panel); font-size: 12px; font-weight: 700; padding-left: 28px; line-height: 21px; }
  .band-work { top: 250px; }
  .band-projects { top: 651px; }

  .side-heading { position: absolute; left: 34px; font-size: 13px; font-weight: 700; letter-spacing: 0.4px; }
  .side-text { position: absolute; left: 34px; width: 186px; font-size: 10.8px; font-weight: 500; line-height: 15.6px; }

  .entries { position: absolute; left: 277px; width: 480px; }
  .entries::before { content: ""; position: absolute; left: 130px; top: -6px; width: 1px; height: 306px; background: var(--rule); }
  .entry { position: relative; height: 163px; display: flex; font-size: 10.8px; line-height: 15.6px; }
  .entry-meta { width: 147px; font-weight: 600; }
  .entry-title { font-weight: 700; }
  .entry-points { list-style: none; font-weight: 600; }
  .entry-points li::before { content: "• "; }
</style>
</head>
<body>
<main class="page">
  <div class="side-panel"></div>
  <div class="header-divider"></div>

  <header class="brand">
    <span class="brand-name">DANIEL REEVE</span>
    <span class="brand-role">CINEMATOGRAPHER</span>
  </header>

  <section class="contact">
    <div class="contact-row"><span class="contact-label">Mobile (Australia):</span><span>+61 400 555 018</span></div>
    <div class="contact-row"><span class="contact-label">Mobile (USA):</span><span>+61 400 555 018</span></div>
    <div class="contact-row"><span class="contact-label">Agent Reel Crew:</span><span>+61 2 9000 4127</span></div>
    <div class="contact-row"><span class="contact-label">Email:</span><span>danielreevedop@mail.com</span></div>
    <div class="contact-row"><span class="contact-label">Website:</span><span>www.danielreeve.com.au</span></div>
  </section>

  <h2 class="side-heading" style="top:295px">ABOUT ME</h2>
  <p class="side-text" style="top:331px">Highly skilled Cinematographer with over 10 years of experience in the film industry. Proven ability to work with large teams and manage all aspects of camera operation and maintenance. Strong background in visual storytelling and post-production editing.</p>

  <h2 class="side-heading" style="top:800px">REFERENCE</h2>
  <p class="side-text" style="top:836px">Lorem ipsum dolor sit amet, consectetur adipiscing elit, sed do eiusmod tempor incididunt ut labore et dolore magna aliqua. Ut enim ad minim veniam, quis nostrud exercitation ullamco laboris nisi ut aliquip ex ea commodo consequat. Duis aute irure dolor in reprehenderit in</p>

  <h2 class="band band-work">WORK EXPERIENCE</h2>
  <section class="entries" style="top:290px">
    <article class="entry">
      <div class="entry-meta">COMPANY NAME<br>ADDRESS<br>DATES</div>
      <div><div class="entry-title">DESIGNATION</div>
        <ul class="entry-points"><li>Lorem ipsum dolor sit amet, consectetur adipiscing</li><li>Sed do eiusmod tempor incididunt ut labore et dolore</li><li>Magna aliqua. Ut enim ad minim veniam, quis nostrud</li><li>Exercitation ullamco laboris nisi ut aliquip ex ea</li><li>Commodo consequat. Duis aute irure dolor in</li><li>Reprehenderit in voluptate velit esse cillum dolore eu</li><li>Fugiat nulla pariatur. Excepteur sint occaecat</li></ul></div>
    </article>
    <article class="entry">
      <div class="entry-meta">COMPANY NAME<br>ADDRESS<br>DATES</div>
      <div><div class="entry-title">DESIGNATION</div>
        <ul class="entry-points"><li>Lorem ipsum dolor sit amet, consectetur adipiscing</li><li>Sed do eiusmod tempor incididunt ut labore et dolore</li><li>Magna aliqua. Ut enim ad minim veniam, quis nostrud</li><li>Exercitation ullamco laboris nisi ut aliquip ex ea</li><li>Commodo consequat. Duis aute irure dolor in</li><li>Reprehenderit in voluptate velit esse cillum dolore eu</li><li>Fugiat nulla pariatur. Excepteur sint occaecat</li></ul></div>
    </article>
  </section>

  <h2 class="band band-projects">PROJECTS</h2>
  <section class="entries" style="top:691px">
    <article class="entry">
      <div class="entry-meta">COMPANY NAME<br>ADDRESS<br>DATES</div>
      <div><div class="entry-title">DESIGNATION</div>
        <ul class="entry-points"><li>Lorem ipsum dolor sit amet, consectetur adipiscing</li><li>Sed do eiusmod tempor incididunt ut labore et dolore</li><li>Magna aliqua. Ut enim ad minim veniam, quis nostrud</li><li>Exercitation ullamco laboris nisi ut aliquip ex ea</li><li>Commodo consequat. Duis aute irure dolor in</li><li>Reprehenderit in voluptate velit esse cillum dolore eu</li><li>Fugiat nulla pariatur. Excepteur sint occaecat</li></ul></div>
    </article>
    <article class="entry">
      <div class="entry-meta">COMPANY NAME<br>ADDRESS<br>DATES</div>
      <div><div class="entry-title">DESIGNATION</div>
        <ul class="entry-points"><li>Lorem ipsum dolor sit amet, consectetur adipiscing</li><li>Sed do eiusmod tempor incididunt ut labore et dolore</li><li>Magna aliqua. Ut enim ad minim veniam, quis nostrud</li><li>Exercitation ullamco laboris nisi ut aliquip ex ea</li><li>Commodo consequat. Duis aute irure dolor in</li><li>Reprehenderit in voluptate velit esse cillum dolore eu</li><li>Fugiat nulla pariatur. Excepteur sint occaecat</li></ul></div>
    </article>
  </section>
</main>
</body>
</html>
```